Makeup Artist Requires Business Card design

Hi

I am looking for a business card design to market my makeup artist business. I operate under my own name Hazel Drummet and I would like to keep the design of the card very simplistic and chic - something that keeps both my name and profession (makeup artist) the focus of the card. I would like it to be a style that is eyecatching to the reader (i am open to anything unusual) but upmarket.

Target Market(s)

women, magazine/beauty/fashion editors, photographers.

Industry/Entity Type

Business

Requirements
Must have
• Must contain:

Phone number: 0417 382 915
Website: www.hazeldrummet.com.au
email: contact@hazeldrummet.com.au

(although you don't need to have prefaced these with the words phone number, website etc :))
Should not have
• I am not looking for anything overly colorful - my preference is to keep the card dark if possible.

```html
<!DOCTYPE html>
<html lang="en">
<head>
<meta charset="utf-8">
<title>Hazel Drummet – Makeup Artist Business Card</title>
<link href="https://fonts.googleapis.com/css2?family=Pinyon+Script&family=Montserrat:wght@400&display=swap" rel="stylesheet">
<style>
  :root {
    --stage: #1b1b1b;
    --card: #262626;
    --card-edge: #2e2e2e;
    --ink: #a3a3a3;
    --ink-soft: #8c8c8c;
    --portrait-light: #d6d6d6;
    --portrait-mid: #9a9a9a;
    --portrait-dark: #4a4a4a;
  }
  * { box-sizing: border-box; margin: 0; padding: 0; }
  html, body {
    width: 1200px;
    height: 901px;
    overflow: hidden;
    background: var(--stage);
  }
  .stage {
    position: relative;
    width: 1200px;
    height: 901px;
    display: flex;
    align-items: center;
    justify-content: center;
    gap: 40px;
  }
  .card {
    position: relative;
    width: 540px;
    height: 310px;
    border-radius: 22px;
    background: var(--card);
    box-shadow: 0 0 0 1px var(--card-edge), 0 18px 40px rgba(0,0,0,0.55);
    overflow: hidden;
  }

  /* Front face */
  .card--front .wordmark {
    position: absolute;
    left: 0;
    right: 0;
    top: 92px;
    text-align: center;
  }
  .wordmark__name {
    display: block;
    font-family: "Pinyon Script", cursive;
    font-size: 72px;
    line-height: 1;
    color: var(--ink);
  }
  .wordmark__role {
    display: block;
    margin-top: 6px;
    padding-left: 190px;
    font-family: "Montserrat", sans-serif;
    font-size: 16px;
    letter-spacing: 0.5px;
    color: var(--ink-soft);
  }

  /* Back face */
  .portrait {
    position: absolute;
    left: -20px;
    top: -25px;
    width: 360px;
    height: 360px;
    border-radius: 50%;
    background: radial-gradient(circle closest-side at 50% 48%,
      var(--portrait-light) 0%,
      #c2c2c2 35%,
      var(--portrait-mid) 65%,
      var(--portrait-dark) 86%,
      var(--card) 100%);
  }
  .contact {
    position: absolute;
    left: 346px;
    top: 92px;
    font-family: "Montserrat", sans-serif;
    color: var(--ink);
    list-style: none;
  }
  .contact__name {
    font-size: 14px;
    margin-bottom: 3px;
  }
  .contact__role {
    font-size: 10.5px;
    color: var(--ink-soft);
    margin-bottom: 20px;
  }
  .contact__line {
    font-size: 10.5px;
    line-height: 1.7;
  }
</style>
</head>
<body>
  <main class="stage">
    <section class="card card--front" aria-label="Card front">
      <div class="wordmark">
        <span class="wordmark__name">Hazel Drummet</span>
        <span class="wordmark__role">Makeup Artist</span>
      </div>
    </section>

    <section class="card card--back" aria-label="Card back">
      <div class="portrait" role="img" aria-label="Black and white portrait photograph of the makeup artist in a soft circular vignette"></div>
      <ul class="contact">
        <li class="contact__name">Hazel Drummet</li>
        <li class="contact__role">Makeup Artist</li>
        <li class="contact__line">0417 382 915</li>
        <li class="contact__line">contact@hazeldrummet.com.au</li>
        <li class="contact__line">www.hazeldrummet.com.au</li>
      </ul>
    </section>
  </main>
</body>
</html>
```